Dental Medical History Form - Content provided

Design a medical history form for a dental practice. Content is provided so all that is needed is the formatting to make it look great and easy to read.

"Patient Information" to include all information contained in top portion of the "Patient Medical History Form" docx file.

"Medical History" should follow the formatting and content of the "Exact Medical History" file as this is what the entry fields look like in our practice software and so we would like it to match.

1st page - Patient info, allergies, medications, antibiotics, joint replacement, pregnancy.

2nd page - Do you have, or have you had, any of the following? . . . . . . .

Target Market(s)

All ages but must be clear enough for elderly to read. Use as much space as possible to keep font size bigger yet keep to two pages

Industry/Entity Type

Dental

Font styles to use
Sans Serif

Requirements
Must have
• All content provided
• Our logo at the top (file provided)
• Century Gothic Font
• Limit to two pages

```html
<!DOCTYPE html>
<html lang="en">
<head>
<meta charset="utf-8">
<title>Confidential Medical History – Harbour Dental</title>
<link href="https://fonts.googleapis.com/css2?family=Questrial&family=Didact+Gothic&display=swap" rel="stylesheet">
<style>
  :root{
    --ink:#4d4d4d;
    --muted:#9b9b9b;
    --rule:#8c8c8c;
    --box:#a8a8a8;
    --paper:#ffffff;
  }
  *{box-sizing:border-box;margin:0;padding:0}
  html,body{width:851px;height:1200px;overflow:hidden;background:var(--paper)}
  body{font-family:"Questrial","Didact Gothic",sans-serif;color:var(--ink);font-size:14px}
  .page{position:relative;width:851px;height:1200px}
  .abs{position:absolute;white-space:nowrap}

  .practice-address{right:41px;top:48px;text-align:right;color:var(--muted);font-size:14px;line-height:17.5px}
  .practice-name{left:233px;top:112px;font-size:20px;color:var(--ink);display:flex;align-items:center;gap:10px}
  .practice-name .mark{width:14px;height:14px;border:1px solid var(--ink)}

  .form-title{left:53px;top:201px;font-size:16.5px;font-weight:700;font-family:"Didact Gothic",sans-serif;letter-spacing:0.2px}

  .field{display:flex;align-items:flex-end;height:18px}
  .field .label{padding-right:2px}
  .field .line{flex:1;border-bottom:1px solid var(--rule);height:14px}
  .col-left{left:53px;width:343px}
  .col-right{left:426px;width:384px}
  .hint{position:absolute;top:19px;font-size:10.5px}

  .section-q{font-family:"Didact Gothic",sans-serif;font-size:14.5px;font-weight:700;letter-spacing:0.1px}

  .box{display:inline-block;width:11px;height:11px;border:1px solid var(--box);vertical-align:-1px;margin-left:3px}
  .opt{font-size:13.5px}
  .num{font-size:14px}

  .write-line{height:0;border-bottom:1px solid var(--rule)}
  .turnover{right:43px;top:1141px;font-size:14px}
</style>
</head>
<body>
<main class="page">

  <header>
    <address class="abs practice-address" style="font-style:normal">
      Harbour Dental<br>3.04/118 Shoreline Rd<br>Kelso Bay NSW 2199<br>(02) 40 555 123
    </address>
    <div class="abs practice-name"><span class="mark"></span>Harbour Dental</div>
  </header>

  <h1 class="abs form-title">CONFIDENTAL MEDICAL HISTORY</h1>

  <section class="patient">
    <div class="abs field col-left" style="top:238px"><span class="label">Name:</span><span class="line"></span>
      <span class="hint" style="left:52px">title</span><span class="hint" style="left:100px">first</span>
      <span class="hint" style="left:192px">middle</span><span class="hint" style="left:303px">last</span></div>
    <div class="abs field col-left" style="top:274px"><span class="label">Address:</span><span class="line"></span></div>
    <div class="abs field col-left" style="top:311px"><span class="label">DOB:</span><span class="line"></span></div>
    <div class="abs field col-left" style="top:346px"><span class="label">Email Address:</span><span class="line"></span></div>
    <div class="abs field col-left" style="top:380px"><span class="label">Phone Number(s):</span><span class="line"></span></div>
    <div class="abs col-left" style="top:414px">Emergency Contact Person:</div>
    <div class="abs field col-left" style="top:446px"><span class="label">Name:</span><span class="line"></span></div>
    <div class="abs field col-left" style="top:478px"><span class="label">Relationship:</span><span class="line"></span></div>
    <div class="abs field col-left" style="top:512px"><span class="label">Phone Number:</span><span class="line"></span>
      <span class="hint" style="left:110px">mobile</span><span class="hint" style="left:202px">work</span>
      <span class="hint" style="left:283px">home</span></div>
  </section>

  <section class="practitioner">
    <div class="abs col-right" style="top:238px">General Practicioner:</div>
    <div class="abs field col-right" style="top:274px"><span class="label">Name:</span><span class="line"></span></div>
    <div class="abs field col-right" style="top:311px"><span class="label">Practice Name:</span><span class="line"></span></div>
    <div class="abs field col-right" style="top:346px"><span class="label">Phone Number:</span><span class="line"></span></div>
    <div class="abs col-right" style="top:380px">Do you have a health fund with dental cover? <span class="opt">&nbsp;yes</span><span class="box"></span> <span class="opt">&nbsp;&nbsp;no</span><span class="box"></span></div>
    <div class="abs field col-right" style="top:414px"><span class="label">If so, what is the name of the fund?</span><span class="line"></span></div>
    <div class="abs field col-right" style="top:446px"><span class="label">Fund number?</span><span class="line"></span></div>
    <div class="abs col-right" style="top:478px">Priority number on card:</div>
    <span class="abs num" style="left:602px;top:478px">0</span>
    <span class="abs num" style="left:628px;top:478px">1</span>
    <span class="abs num" style="left:654px;top:478px">2</span>
    <span class="abs num" style="left:679px;top:478px">3</span>
    <span class="abs num" style="left:705px;top:478px">4</span>
    <span class="abs num" style="left:731px;top:478px">5</span>
    <div class="abs field col-right" style="top:512px"><span class="label">Occupation:</span><span class="line"></span></div>
    <div class="abs field col-right" style="top:545px"><span class="label">Referred by:</span><span class="line"></span></div>
  </section>

  <section class="allergies">
    <h2 class="abs section-q" style="left:53px;top:606px">Please indicate if &nbsp;you are allergic to any of the following:</h2>
    <span class="abs opt" style="left:53px;top:640px">Aspirin<span class="box"></span></span>
    <span class="abs opt" style="left:139px;top:640px">Codeine<span class="box"></span></span>
    <span class="abs opt" style="left:240px;top:640px">Penicillin<span class="box"></span></span>
    <span class="abs opt" style="left:338px;top:640px">Sulfites<span class="box"></span></span>
    <span class="abs opt" style="left:425px;top:640px">Latex<span class="box"></span></span>
    <span class="abs opt" style="left:505px;top:640px">Local Anaesthetic<span class="box"></span></span>
    <span class="abs opt" style="left:667px;top:638px">Lactose<span class="box"></span></span>
    <span class="abs opt" style="left:761px;top:640px">Nickel<span class="box"></span></span>
    <div class="abs field" style="left:53px;width:757px;top:662px"><span class="label">Other:</span><span class="line"></span></div>
  </section>

  <section class="medications">
    <h2 class="abs section-q" style="left:53px;top:699px">Are you currently taking, or have ever taken, any of the following medication?</h2>
    <span class="abs opt" style="right:683px;top:732px">Asthma inhaler<span class="box"></span></span>
    <span class="abs opt" style="right:495px;top:732px">Insulin<span class="box"></span></span>
    <span class="abs opt" style="right:342px;top:732px">Blood Pressure<span class="box"></span></span>
    <span class="abs opt" style="right:148px;top:732px">Oral Contraceptive<span class="box"></span></span>
    <span class="abs opt" style="right:683px;top:756px">Chemotherapy<span class="box"></span></span>
    <span class="abs opt" style="right:495px;top:756px">Anti-depressants<span class="box"></span></span>
    <span class="abs opt" style="right:342px;top:756px">Steroids<span class="box"></span></span>
    <span class="abs opt" style="right:148px;top:755px">Bisphosponates<span class="box"></span></span>
    <span class="abs opt" style="right:683px;top:780px">Anti-epileptics<span class="box"></span></span>
    <span class="abs opt" style="right:495px;top:779px">Immunosuppresants<span class="box"></span></span>
    <span class="abs opt" style="right:342px;top:780px">Blood Thinners<span class="box"></span></span>
    <span class="abs opt" style="right:148px;top:781px">Other<span class="box"></span></span>

    <h2 class="abs section-q" style="left:53px;top:822px">Please specify medication name, dose, and frequency where possible.</h2>
    <div class="abs write-line" style="left:51px;width:237px;top:863px"></div>
    <div class="abs write-line" style="left:301px;width:236px;top:863px"></div>
    <div class="abs write-line" style="left:551px;width:259px;top:863px"></div>
    <div class="abs write-line" style="left:51px;width:237px;top:884px"></div>
    <div class="abs write-line" style="left:301px;width:236px;top:884px"></div>
    <div class="abs write-line" style="left:551px;width:259px;top:884px"></div>
    <div class="abs write-line" style="left:51px;width:237px;top:907px"></div>
    <div class="abs write-line" style="left:301px;width:236px;top:907px"></div>
    <div class="abs write-line" style="left:551px;width:259px;top:907px"></div>
  </section>

  <section class="questions">
    <h2 class="abs section-q" style="left:53px;top:929px">Do you require antibiotic cover?</h2>
    <span class="abs opt" style="left:313px;top:928px">yes<span class="box"></span></span>
    <span class="abs opt" style="left:368px;top:927px">no<span class="box"></span></span>

    <h2 class="abs section-q" style="left:53px;top:965px">Have you had a joint replacement?</h2>
    <span class="abs opt" style="left:313px;top:965px">yes<span class="box"></span></span>
    <span class="abs opt" style="left:368px;top:964px">no<span class="box"></span></span>

    <h2 class="abs section-q" style="left:53px;top:999px">Are you pregnant?</h2>
    <span class="abs opt" style="left:313px;top:1000px">yes<span class="box"></span></span>
    <span class="abs opt" style="left:368px;top:999px">no<span class="box"></span></span>
    <h2 class="abs section-q" style="left:463px;top:1001px">Breastfeeding?</h2>
  </section>

  <footer class="abs turnover">please turnover</footer>
</main>
</body>
</html>
```